Protrait photographers business card

Need a new catchy, chic business card to promote my new portrait photograghy business. Love taking the natural, location portraits of families, children, teens. It should look classy, but also warm & friendly. I want it to show that Famliy, friends, couples & childten are what I love photographing, so if it can have that sort of feel to it & also looking energetic.

Target Market(s)

Families, couples, babies, people on holidays wanting some locational professional photos

Industry/Entity Type

Portrait Photography

Contact Information for Business Card

Marisol photography, By Tavi, Lorna Brackwell,Ph: 0437586204, Pelican reach, Qld

Font styles to use
Decorative
Script

Requirements
Must have
• Company name & photographers name
Nice to have
• a coloured card
Should not have
• not be on a white card

```html
<!DOCTYPE html>
<html lang="en">
<head>
<meta charset="UTF-8">
<title>Marisol photography – Business Card</title>
<link href="https://fonts.googleapis.com/css2?family=Poiret+One&display=swap" rel="stylesheet">
<style>
  :root {
    --page-bg: #ecebe8;
    --card-dark: #1f1f1f;
    --card-mid: #3a3a3a;
    --accent-yellow: #f2ec2e;
    --text-light: #f4f4f4;
    --text-dark: #1c1c1c;
    --photo-light: #bdbdbd;
    --photo-dark: #2b2b2b;
  }
  * { margin: 0; padding: 0; box-sizing: border-box; }
  html, body {
    width: 1200px;
    height: 800px;
    overflow: hidden;
    background: var(--page-bg);
  }
  .canvas {
    width: 1200px;
    height: 800px;
    display: flex;
    align-items: center;
    justify-content: center;
  }
  .business-card {
    position: relative;
    width: 1050px;
    height: 600px;
    overflow: hidden;
    background: linear-gradient(160deg, var(--card-mid) 0%, var(--card-dark) 55%, #2a2a2a 100%);
    font-family: "Poiret One", sans-serif;
    box-shadow: 0 10px 30px rgba(0,0,0,0.18);
  }
  .portrait-area {
    position: absolute;
    left: 0;
    top: 0;
    width: 560px;
    height: 100%;
    background:
      radial-gradient(ellipse 45% 40% at 45% 38%, var(--photo-light) 0%, #8a8a8a 45%, transparent 80%),
      linear-gradient(90deg, #6d6d6d 0%, #4a4a4a 55%, rgba(40,40,40,0) 100%);
  }
  .contact-details {
    position: absolute;
    left: 595px;
    top: 30px;
    color: var(--text-light);
    font-size: 44px;
    line-height: 62px;
    letter-spacing: 1px;
  }
  .social-band {
    position: absolute;
    left: 545px;
    top: 290px;
    width: 505px;
    height: 150px;
    background: var(--accent-yellow);
    border-radius: 75px 0 0 75px;
    padding: 12px 0 0 70px;
    color: var(--text-dark);
    font-size: 32px;
    line-height: 42px;
  }
  .social-line {
    display: flex;
    align-items: center;
    gap: 10px;
  }
  .social-line svg { flex: none; }
  .social-dot {
    width: 18px;
    height: 18px;
    border-radius: 50%;
    background: var(--text-dark);
    flex: none;
  }
  .brand-name {
    position: absolute;
    left: 55px;
    top: 455px;
    color: var(--accent-yellow);
    font-size: 56px;
    line-height: 54px;
    letter-spacing: 1px;
  }
</style>
</head>
<body>
<div class="canvas">
  <div class="business-card">
    <div class="portrait-area" role="img" aria-label="Black and white portrait photograph of a young woman with wavy hair"></div>

    <div class="contact-details">
      <p class="photographer-name">Lorna Brackwell</p>
      <p class="phone">0437586204</p>
      <p class="locality">Pelican Reach,</p>
      <p class="state">Queensland</p>
    </div>

    <div class="social-band">
      <p class="social-line">
        <svg width="20" height="16" viewBox="0 0 20 16" aria-hidden="true">
          <rect x="1" y="1" width="18" height="14" fill="none" stroke="#1c1c1c" stroke-width="2"/>
          <path d="M1 1 L10 9 L19 1" fill="none" stroke="#1c1c1c" stroke-width="2"/>
        </svg>
        hello@marisolphoto.com
      </p>
      <p class="social-line"><span class="social-dot"></span>pagebook.com/tavi123</p>
      <p class="social-line"><span class="social-dot"></span>chirper.com/tavi123</p>
    </div>

    <div class="brand-name">
      <p>Marisol photography</p>
      <p>By Tavi</p>
    </div>
  </div>
</div>
</body>
</html>
```